Book cover for a book about time management for women

We need a book cover for a book about time management for women written by a woman. Even though the book has a provocative title "Calendar candy" based on the seminars the author holds for women seeking the change in their life, it has nothing to do with the words themselves. The subtitle is "Keep each morning in your grip. A bold guide on daily rhythm for ladies today"

Preferred fonts (not necessarily):
Plus Jakarta Sans
Tiempos Headline

Preferred colours (not necessarily):
- orange
- pastel "highlighters"

We look for a simple/clean design that catches the attention of the women without too many graphic elements.

Target Market(s)

Women that want to change and organise their life

Industry/Entity Type

productivity, marketing, work-life balance

Font styles to use
Other font styles liked:
• Plus Jakarta Sans, Tiempos Headline

Colors
F0912C
F2A743
F7CA91
FBE8D2
FDF5EE
A7469A
B969AE
D3A5CF
EDDBEB
F8F0F9

Requirements
Must have
• Famine feeling as the target audience are women with drive to better life
Should not have
• No explicit images or sexually motivated themes

```html
<!DOCTYPE html>
<html lang="en">
<head>
<meta charset="utf-8">
<title>Calendar Candy – Book Cover</title>
<link rel="stylesheet" href="https://fonts.googleapis.com/css2?family=Plus+Jakarta+Sans:wght@300;400;500&family=Source+Serif+4:opsz,wght@8..60,600;8..60,700&display=swap">
<style>
  :root {
    --backdrop: #000000;
    --cover-purple: #9d4f9f;
    --band-plum: #7a2d72;
    --band-orange: #f0802e;
    --accent-orange: #eb9540;
    --ink-white: #ffffff;
    --photo-light: #c9a7c8;
    --photo-dark: #6e3a70;
  }
  * { margin: 0; padding: 0; box-sizing: border-box; }
  html, body {
    width: 1200px;
    height: 1200px;
    overflow: hidden;
    background: var(--backdrop);
  }
  .canvas {
    position: relative;
    width: 1200px;
    height: 1200px;
  }
  .book-cover {
    position: absolute;
    left: 360px;
    top: 240px;
    width: 480px;
    height: 720px;
    background: var(--cover-purple);
    overflow: hidden;
  }
  .tagline-band {
    position: absolute;
    left: 0; top: 0;
    width: 100%;
    height: 49px;
    background: var(--band-orange);
    display: flex;
    align-items: center;
    justify-content: center;
    font-family: "Plus Jakarta Sans", sans-serif;
    font-weight: 500;
    font-size: 15.5px;
    color: var(--ink-white);
    text-transform: uppercase;
    white-space: nowrap;
  }
  .cover-photo {
    position: absolute;
    left: 0;
    top: 62px;
    width: 300px;
    height: 300px;
    border-radius: 0 150px 150px 0;
    background: radial-gradient(circle at 65% 62%, var(--photo-light) 0%, var(--photo-dark) 75%);
    opacity: 0.85;
  }
  .title {
    position: absolute;
    left: 0;
    width: 100%;
    text-align: center;
    font-family: "Source Serif 4", serif;
    color: var(--ink-white);
    text-transform: uppercase;
    line-height: 1;
  }
  .title-kicker {
    top: 356px;
    font-weight: 700;
    font-size: 52px;
    letter-spacing: 0.01em;
  }
  .title-main {
    top: 412px;
    font-weight: 600;
    font-size: 122px;
    letter-spacing: 0.01em;
  }
  .subtitle {
    position: absolute;
    left: 0;
    top: 548px;
    width: 100%;
    text-align: center;
    font-family: "Plus Jakarta Sans", sans-serif;
    font-weight: 300;
    font-size: 30px;
    line-height: 50px;
    letter-spacing: 0.12em;
    color: var(--accent-orange);
    text-transform: uppercase;
  }
  .author-band {
    position: absolute;
    left: 0; bottom: 0;
    width: 100%;
    height: 68px;
    background: var(--band-plum);
    display: flex;
    align-items: center;
    justify-content: center;
    font-family: "Plus Jakarta Sans", sans-serif;
    font-weight: 400;
    font-size: 20px;
    letter-spacing: 0.14em;
    color: var(--ink-white);
    text-transform: uppercase;
  }
</style>
</head>
<body>
  <main class="canvas">
    <section class="book-cover">
      <div class="tagline-band">A bold guide on daily rhythm for ladies today</div>
      <div class="cover-photo" role="img" aria-label="Black and white photo of a hand holding a ringing alarm clock by its handle"></div>
      <h1 class="title title-kicker">Calendar</h1>
      <div class="title title-main">Candy</div>
      <p class="subtitle">Keep each morning<br>in your grip</p>
      <div class="author-band">Author Names</div>
    </section>
  </main>
</body>
</html>
```